Creating High Performance Leadership Teams

I periodically write articles that I sent out to executive and Senior leaders. They should be reproducable in print form yet most of them will go out in pdf Format. I have attached a recent example that we did and I would like to see what you can do with the second example I have attached.

The Format should ideally fit in an A3 Format.

Target Market(s)

Executive and Senior Leaders

Industry/Entity Type

Leadership

Font styles to use
Other font styles liked:
• we often use calibri

Requirements
Must have
• Fit on a A3 paper Format, like the example I sent
Nice to have
• Should look highly professional, perhaps picutures or graphics to Support the text, a Little bit like the Maplecroft Trade Quarterly Articles (MTQ) although mine are shorter.
• You will see our Color formatting by visiting our Website, www.cortavo-insight.com

```html
<!DOCTYPE html>
<html lang="en">
<head>
<meta charset="utf-8">
<title>Creating High Performance Leadership Teams</title>
<link href="https://fonts.googleapis.com/css2?family=Carlito:ital,wght@0,400;0,700;1,400&display=swap" rel="stylesheet">
<style>
  :root {
    --ink: #222222;
    --muted: #555555;
    --teal: #2a8c9c;
    --accent: #e8892b;
    --rule: #bfc5c8;
    --paper: #ffffff;
    --photo-a: #8fa3b0;
    --photo-b: #d7b59a;
  }
  html, body {
    margin: 0;
    padding: 0;
    width: 849px;
    height: 1200px;
    overflow: hidden;
    background: var(--paper);
  }
  .page {
    position: relative;
    width: 849px;
    height: 1200px;
    font-family: "Carlito", "Calibri", sans-serif;
    color: var(--ink);
    font-size: 16.5px;
    line-height: 22px;
  }
  .running-head {
    position: absolute;
    left: 28px;
    top: 8px;
    right: 28px;
    font-size: 9px;
    line-height: 11px;
    color: var(--muted);
    padding-bottom: 4px;
    border-bottom: 0.8px solid var(--rule);
  }
  .intro {
    position: absolute;
    left: 28px;
    top: 32px;
    width: 793px;
    margin: 0;
  }
  .hero {
    position: absolute;
    left: 28px;
    top: 174px;
    width: 793px;
    height: 392px;
    background: linear-gradient(135deg, var(--photo-a) 0%, #c9ced2 45%, var(--photo-b) 100%);
  }
  .column {
    position: absolute;
    top: 578px;
    width: 390px;
    hyphens: auto;
    -webkit-hyphens: auto;
  }
  .column p { margin: 0; }
  .col-left { left: 28px; }
  .col-right { left: 431px; }
  .pull-quote {
    margin: 18px 0 0 0;
    padding: 14px 20px 16px 18px;
    border-top: 1px solid var(--rule);
    border-bottom: 1px solid var(--rule);
    color: var(--teal);
    font-weight: 700;
    font-size: 27px;
    line-height: 34px;
    hyphens: none;
    -webkit-hyphens: none;
  }
  .pull-quote span {
    display: block;
    border-left: 4px solid var(--accent);
    padding-left: 14px;
    width: 300px;
  }
  .bullets {
    list-style: none;
    margin: 0;
    padding: 0;
  }
  .bullets li {
    position: relative;
    padding-left: 12px;
  }
  .bullets li::before {
    content: "•";
    position: absolute;
    left: 0;
  }
  strong { font-weight: 700; }
  .footer {
    position: absolute;
    left: 28px;
    right: 28px;
    bottom: 8px;
    padding-top: 4px;
    border-top: 0.8px solid var(--rule);
    font-size: 9px;
    line-height: 11px;
    color: var(--muted);
    text-align: right;
  }
</style>
</head>
<body>
<div class="page">
  <div class="running-head">Creating High Performance Leadership Teams</div>

  <p class="intro">Over the last 25 years, I have developed and coached leaders, teams and talents in a significant number of global organizations and I am convinced that helping leadership teams become exceptional remains the single most valuable investment an organization can make if they truly want to become a first class company. <strong>Leadership teams makes a difference. Research shows that the effectiveness of executive leadership teams have a huge impact on organizational climate and performance.</strong> All the more reason to give executive and senior team leadership warranted attention and investment.</p>

  <div class="hero" role="img" aria-label="Photograph of many hands stacked together in the centre, a symbol of team unity"></div>

  <div class="column col-left">
    <p>Powerful benefits come to the organization after leadership teams earnestly agree that they have room to improve and publicly acknowledge the development process they are undertaking. The humility, discipline and courage to work on their leadership team issues is a powerful Vorbild for the entire company. This creates a climate for growth and improvement for everyone.</p>
    <p>Leadership teams that learn from and with each other create the conditions for compounding learning, and like compound interest, it grows exponentially. <strong>If the senior leaders are not setting the example of</strong></p>
    <div class="pull-quote"><span>Helping leadership teams become exceptional remains the single most valuable investment an organization can make if they truly want to become a first class company</span></div>
  </div>

  <div class="column col-right">
    <p><strong>learning, adapting and changing for the people they lead, who is?</strong></p>
    <p>At the end of the day, if each and every leadership team in the organization is not deliberately aiming to become an exceptional team and perform individually and collectively in an exceptional way, why should anyone else?</p>
    <p>I have worked with dozens of leadership teams in Europe, the USA and Asia and I've not found one that didn't have some potential to develop and improve. <strong>In the following article, I'll share the seven insights to becoming a real leadership team, one that creates exceptional performance and results.</strong> These insights highlight what must go right and what can go wrong in respect to senior leader teams. Before sharing the seven insights, I'm assuming the following are in place with your team:</p>
    <ul class="bullets">
      <li>The senior leadership team members are ethically and morally sound</li>
      <li>As individual team members they are hard-working, results oriented and have earned their seat at the leadership team table</li>
      <li>Each member is fit and competent in the functional aspect of their role</li>
    </ul>
  </div>

  <div class="footer">© 2015 Mara Lindqvist, Cortavo Insight Solutions GmbH, Munich, Germany</div>
</div>
</body>
</html>
```